Cleaning services Business Card Design

I need a business card design for my Cleaning business. I would like perhaps emphasis on the company name, Muddle to Marvel. Maybe the Muddle would to dirty and the marvel would have sprinkles.

Industry/Entity Type

Business

Contact Information for Business Card

Muddle to Marvel Cleaning Services, Teodoro Perlas, Industrial, Commercial, & Residential 418-635-0247

```html
<!DOCTYPE html>
<html lang="en">
<head>
<meta charset="utf-8">
<title>Muddle to Marvel Cleaning Services – Business Card</title>
<link rel="stylesheet" href="https://fonts.googleapis.com/css2?family=Cinzel:wght@400;700&family=Tinos&display=swap">
<style>
  :root {
    --backdrop: #8e9096;
    --charcoal: #3a3839;
    --sky: #5bb8ea;
    --paper: #ffffff;
    --ink: #231f20;
  }
  * { margin: 0; padding: 0; box-sizing: border-box; }
  html, body {
    width: 1200px; height: 800px; overflow: hidden;
    background: var(--backdrop);
  }
  .card {
    position: absolute; left: 100px; top: 110px;
    width: 1000px; height: 580px;
    background: var(--paper);
    overflow: hidden;
    box-shadow: 0 10px 30px rgba(0,0,0,.25);
  }
  .card-shapes { position: absolute; inset: 0; }
  .brand-name {
    position: absolute; left: 105px; top: 150px; width: 330px;
    text-align: center;
    font-family: "Cinzel", serif; font-weight: 700;
    font-size: 38px; line-height: 1.2; color: var(--sky);
  }
  .contact { position: absolute; left: 560px; top: 165px; }
  .contact-name {
    font-family: "Cinzel", serif; font-size: 28px;
    color: var(--sky); letter-spacing: 1px; margin-left: 45px;
  }
  .contact-phone {
    display: flex; align-items: center; gap: 14px; margin-top: 24px;
    font-family: "Tinos", serif; font-size: 34px; color: var(--paper);
  }
  .services { position: absolute; left: 520px; top: 318px; }
  .services-title {
    font-family: "Cinzel", serif; font-size: 30px; color: var(--ink);
  }
  .services-list { list-style: none; margin: 12px 0 0 50px; }
  .services-list li {
    font-family: "Cinzel", serif; font-size: 22px; line-height: 28px; color: var(--ink);
    display: flex; align-items: center; gap: 10px; margin-bottom: 8px;
  }
  .services-list li::before {
    content: ""; width: 12px; height: 12px; border-radius: 50%;
    background: var(--sky);
  }
</style>
</head>
<body>
  <div class="card">
    <svg class="card-shapes" width="1000" height="580" viewBox="0 0 1000 580">
      <polygon points="0,0 1000,0 1000,325 0,232" fill="var(--charcoal)"/>
      <rect x="0" y="515" width="1000" height="40" fill="var(--sky)"/>
      <path d="M90,515 C140,515 150,548 225,548 C300,548 310,515 360,515 Z" fill="var(--paper)"/>
      <circle cx="270" cy="245" r="172" fill="var(--paper)" stroke="var(--sky)" stroke-width="6"/>
    </svg>

    <div class="brand-name">Muddle to Marvel Cleaning Services</div>

    <div class="contact">
      <div class="contact-name">Teodoro Perlas</div>
      <div class="contact-phone">
        <svg width="30" height="30" viewBox="0 0 30 30" aria-hidden="true">
          <circle cx="15" cy="15" r="15" fill="var(--sky)"/>
          <path d="M10 8c1-1 2-1 3 0l1 2c.5 1 0 2-1 2.5 0 1.5 2 4 3.5 4.5.5-1 1.5-1.5 2.5-1l2 1c1 1 1 2 0 3-2 2-5 1-8-2s-5-7-3-10z" fill="var(--paper)"/>
        </svg>
        <span>418-635-0247</span>
      </div>
    </div>

    <div class="services">
      <div class="services-title">Cleaning Services:</div>
      <ul class="services-list">
        <li>Industrial</li>
        <li>Commercial</li>
        <li>Residential</li>
      </ul>
    </div>
  </div>
</body>
</html>
```